Wendy Marsh Copywriter Website

I am starting a new business as a freelance copywriter. Trying to set up the website for my business is proving to be too technical for me. I would like a simple, clean website using primarily black and white. I have attached the logo I would like used. I would like the menu icons to be Home, Services, Portfolio, Blog, Contact. I would like my mobile phone number (0412 583 906) and email address (wendy.marsh.copywriter@mailbox-example.com) used in the header of the site. I need the site to be easily manageable and inter-changeable for me to be able to move things around and add images, etc with ease.

I would like the home page to be a static page with space for an image of myself somewhere (I haven't had this taken as yet), an area to put a bit about myself and my business, and also somewhere to include social media icons/links. Again, I would like the whole website and home page to be easily managed so that I can add/delete things with ease.

I would like the image of the typewriter used in the website somewhere also please.

Font styles to use
Sans Serif
Script

Colors
fdf0f6

Requirements
Must have
• The logo provided
• Ability to change page contents easily
• Ability to add social media icons as needed
Nice to have
• Use of the typewriter image
Should not have
• Complicated pages that are not easily editable

```html
<!DOCTYPE html>
<html lang="en">
<head>
<meta charset="utf-8">
<title>Wendy Marsh Copywriter</title>
<link rel="stylesheet" href="https://fonts.googleapis.com/css2?family=Tinos:wght@400;700&family=Barlow+Condensed:wght@600&family=Pinyon+Script&display=swap">
<style>
:root{
  --ink:#000;
  --paper:#fff;
  --mist:#f4f4f4;
  --blush:#fdf0f6;
  --brush:#f1e4e6;
  --machine-dark:#1a1a1a;
  --machine-mid:#555;
  --avatar:#c4c4c4;
  --rule:#bdbdbd;
}
*{box-sizing:border-box;margin:0;padding:0}
html,body{width:983px;height:1200px;overflow:hidden;background:var(--paper)}
body{position:relative;font-family:"Tinos","Times New Roman",serif;color:var(--ink)}
.abs{position:absolute}

.contact-bar{top:7px;left:0;width:983px;height:14px;font-size:9.5px}
.contact-bar .phone{position:absolute;left:347px}
.contact-bar .email{position:absolute;left:474px}

.hero-image{left:425px;top:90px;width:134px;height:208px;
  background:linear-gradient(180deg,#ececec 0 28%,var(--machine-mid) 28%,var(--machine-dark) 60%,#3a3a3a 100%);border-radius:4px}

.brand-stroke{left:404px;top:325px;width:175px;height:33px;background:var(--brush);border-radius:14px}
.brand-name{left:404px;top:326px;width:175px;text-align:center;font-size:17px;line-height:20px;color:var(--ink)}
.brand-role{left:404px;top:346px;width:175px;text-align:center;font-size:5.5px;letter-spacing:3px;color:var(--ink)}

.main-nav{top:452px;left:0;width:983px;height:12px;font-size:8px;font-weight:700;letter-spacing:1.3px}
.main-nav a{position:absolute;color:var(--ink);text-decoration:none}

.about{left:0;top:468px;width:983px;height:371px;background:var(--mist)}
.about-title{position:absolute;top:108px;left:0;width:983px;text-align:center;font-family:"Pinyon Script",cursive;font-size:14px}
.avatar{position:absolute;left:215px;top:136px;width:43px;height:43px;border-radius:50%;background:var(--avatar)}
.about-text{position:absolute;left:215px;width:553px;text-align:center;font-size:9.2px;line-height:14.8px}
.about-text.lead{top:136px;padding-left:53px}
.about-text.body{top:195px}

.site-footer{left:0;top:839px;width:983px;height:361px;background:var(--ink);color:var(--paper)}
.footer-heading{position:absolute;top:100px;width:200px;text-align:center;font-family:"Barlow Condensed",sans-serif;font-weight:600;font-size:11px;letter-spacing:1px}
.social-link{position:absolute;top:127px;width:27px;height:27px;background:var(--blush)}
.page-links{position:absolute;left:400px;top:122px;width:184px;list-style:none}
.page-links li{height:24px;border-bottom:1px solid var(--rule);text-align:center;font-size:8px;line-height:22px}
.page-links a{color:var(--paper)}
.field{position:absolute;height:26px;border:1px solid var(--rule);font-size:7.5px;line-height:24px;padding-left:8px}
.join-btn{position:absolute;left:740px;top:162px;width:58px;height:27px;border:1px solid var(--rule);text-align:center;font-family:"Barlow Condensed",sans-serif;font-weight:600;font-size:8.5px;line-height:25px;letter-spacing:1px}
.credit{position:absolute;top:297px;left:0;width:983px;text-align:center;font-size:7px}
.credit svg{vertical-align:-1px;margin:0 3px}
</style>
</head>
<body>

<div class="abs contact-bar">
  <span class="phone">Ph:(+61) 0412 583 906</span>
  <span class="email">Email: wendy.marsh.copywriter@mailbox-example.com</span>
</div>

<div class="abs hero-image" role="img" aria-label="Photograph of a vintage black typewriter with a sheet of paper"></div>

<div class="abs brand-stroke" role="img" aria-label="Soft pink brush stroke behind the brand name"></div>
<div class="abs brand-name">Wendy Marsh</div>
<div class="abs brand-role">copywriter</div>

<nav class="abs main-nav">
  <a href="#" style="left:345px">HOME</a>
  <a href="#" style="left:397px">SERVICES</a>
  <a href="#" style="left:467px">PORTFOLIO</a>
  <a href="#" style="left:545px">BLOG</a>
  <a href="#" style="left:596px">CONTACT</a>
</nav>

<section class="abs about">
  <h2 class="about-title">About</h2>
  <div class="avatar" role="img" aria-label="Placeholder for a portrait photo"></div>
  <p class="about-text lead">Lorem ipsum dolor sit amet, consectetur adipiscing elit. Morbi ut porta libero. Proin nec porta orci. Aliquam erat volutpat. Morbi sit amet tristique libero. Phasellus malesuada mattis risus, vel ultricies est egestas sed. Ut dignissim fringilla vehicula. Pellentesque ut hendrerit magna.</p>
  <p class="about-text body">Curabitur sit amet diam imperdiet, bibendum massa vitae, consequat nunc. Vivamus laoreet id elit ut fringilla. Vivamus tincidunt leo eget dui rhoncus egestas. Nunc sed pellentesque elit. Pellentesque lobortis erat nec ex consequat tristique. Proin in lacinia mi. Phasellus eget auctor lorem. Donec euismod, quam eu feugiat interdum, dui lacus eleifend mauris, ac fermentum lorem lectus vel leo. Nam et porta lacus. Vestibulum at nisl felis. Ut vestibulum tristique quam sed consectetur. Nunc fermentum porttitor arcu ac vehicula. Maecenas sagittis, mi a euismod tempus, lorem nisl tempus lacus, eu facilisis urna enim eu ex.</p>
</section>

<footer class="abs site-footer">
  <h3 class="footer-heading" style="left:176px">FIND ME</h3>
  <a class="social-link" href="#" style="left:197px" aria-label="Social link one"></a>
  <a class="social-link" href="#" style="left:230px" aria-label="Social link two"></a>
  <a class="social-link" href="#" style="left:263px" aria-label="Social link three"></a>
  <a class="social-link" href="#" style="left:296px" aria-label="Social link four"></a>
  <a class="social-link" href="#" style="left:329px" aria-label="Social link five"></a>

  <h3 class="footer-heading" style="left:391px">PAGES</h3>
  <ul class="page-links">
    <li><a href="#">Home</a></li>
    <li><a href="#">Portfolio</a></li>
    <li><a href="#">Blog</a></li>
    <li><a href="#">Contact</a></li>
    <li><a href="#">Services</a></li>
  </ul>

  <h3 class="footer-heading" style="left:606px">JOIN ME</h3>
  <div class="field" style="left:614px;top:128px;width:184px">First Name</div>
  <div class="field" style="left:614px;top:162px;width:121px">E-Mail Address</div>
  <div class="join-btn">JOIN</div>

  <p class="credit">Handcrafted with<svg width="8" height="7" viewBox="0 0 10 9"><path d="M5 9 0.8 4.7A2.5 2.5 0 0 1 5 1.4 2.5 2.5 0 0 1 9.2 4.7Z" fill="#fff"/></svg>on the Keystone Framework</p>
</footer>

</body>
</html>
```